Label or packaging Design for Hair Care Line

Dear Designer,
We are Corvella, a brand known for our premium hairstyling tools, and we are excited to expand into hair care. We are currently looking for a talented designer to create the label designs for our entire luxury hair care line.
This project is crucial in establishing our visual identity in the hair care market, and we aim to position ourselves alongside premium brands such as LTP, Dorvane Hair Atelier, and Pelmi.
Project Scope
We need a cohesive label design for our hair care line, which includes:
5 products (e.g., shampoo, conditioner, hair oil, styling cream, and a hair mask).
The designs should include:
Front label: Highlighting the product name, key features, and branding.
Our goal is to achieve a design that communicates premium luxury with a touch of professionalism. Below are the specific guidelines to help you align with our vision:
Style and Inspiration
Think of brands like LTP, Dorvane Hair Atelier, and Pelmi.
Luxury and Minimalism: Clean lines, sophisticated typography, and an elegant color palette.
Subtle femininity: premium finishes like metallic accents (gold, silver, or rose gold).
Brand Personality
Premium: Reflecting high quality and exclusivity.
Modern & Professional: Appealing to a refined, professional audience but also suitable for lifestyle-oriented customers.
Warm & Empowering: A brand that celebrates confidence and individuality.
Color Palette
Neutral tones like black, white, accented with metallics (gold or silver) for a luxurious feel.
Colors that feel timeless and elegant rather than trendy or overly bright.
Typography
Use clean, modern fonts (preferably sans-serif or serif for a refined look).
Clear and legible for all product details while maintaining a high-end aesthetic.
Materials and Finishes
Packaging Shape
The label designs should suit a variety of bottle and jar shapes (e.g., cylindrical, flat, or rounded).
Keep scalability in mind so the identity remains consistent across different products.
Deliverables
To understand the aesthetic we are aiming for, here are some brands to use as inspiration:
LTP: For its minimalistic and modern approach.
Dorvane Hair Atelier: For its combination of luxury and professional appeal.
Pelmi: For its soft femininity and lifestyle branding.
we would like to see your designs applied to a variety of packaging types to get an overall impression of how the brand identity works across different product formats. This includes:
A squeeze bottle (e.g., for styling creams or conditioners).
A glass bottle with a dropper (e.g., for a luxurious hair oil).
A shampoo/conditioner bottle (standard pump or flip-top cap).
A spray bottle (e.g., for leave-in treatments or heat protectors).
By creating designs for these different packaging types, we can better evaluate how cohesive and versatile the brand identity will be across the entire product line.

Updates
As you may have noticed from the designs, they don’t quite align with our briefing. The look needs to be clean and professional, similar to Dorvane, LTP, and the other examples we provided. Please address this, and we’ll check it!

Target Market(s)
europe and us
Font styles to use
Other font styles liked:
- century gothic

Look and feel
Each slider illustrates characteristics of the customer's brand and the style your logo design should communicate.

```html
<!DOCTYPE html>
<html lang="en">
<head>
<meta charset="UTF-8">
<title>Corvella Revitalizing Shampoo Label</title>
<link href="https://fonts.googleapis.com/css2?family=Questrial&display=swap" rel="stylesheet">
<style>
  :root {
    --paper: #ffffff;
    --label-black: #050505;
    --band-grey: #1b1b1b;
    --band-grey-light: #2a2a2a;
    --gold: #c99a4c;
    --gold-light: #f0c777;
    --gold-deep: #8a5a1e;
    --text-white: #f2f2f2;
    --text-grey: #b8b8b8;
  }
  * { margin: 0; padding: 0; box-sizing: border-box; }
  html, body {
    width: 670px;
    height: 1200px;
    overflow: hidden;
    background: var(--paper);
    font-family: "Questrial", sans-serif;
  }
  .label {
    position: absolute;
    left: 26px;
    top: 8px;
    width: 618px;
    height: 1184px;
    background: var(--label-black);
    overflow: hidden;
  }
  .gold-dust {
    position: absolute;
    right: 0;
    top: 0;
    width: 420px;
    height: 300px;
    background: radial-gradient(ellipse at 85% 25%, rgba(201,154,76,0.35) 0%, rgba(201,154,76,0.12) 40%, rgba(0,0,0,0) 70%);
  }
  .brand-name {
    position: absolute;
    top: 262px;
    width: 100%;
    text-align: center;
    color: var(--text-white);
    font-size: 62px;
    letter-spacing: 1px;
  }
  .range-band {
    position: absolute;
    top: 382px;
    left: 0;
    width: 100%;
    height: 58px;
    background: linear-gradient(90deg, var(--label-black) 0%, var(--band-grey) 30%, var(--band-grey) 70%, var(--label-black) 100%);
    display: flex;
    align-items: center;
    justify-content: center;
  }
  .range-name {
    color: var(--text-grey);
    font-size: 36px;
    letter-spacing: 13px;
    padding-left: 13px;
  }
  .product-name {
    position: absolute;
    top: 456px;
    width: 100%;
    text-align: center;
    font-size: 92px;
    letter-spacing: 3px;
    background: linear-gradient(180deg, var(--gold-light) 0%, var(--gold) 55%, var(--gold-deep) 100%);
    -webkit-background-clip: text;
    background-clip: text;
    color: transparent;
  }
  .key-ingredients {
    position: absolute;
    top: 570px;
    left: 0;
    width: 100%;
    padding-left: 210px;
    color: var(--gold);
    font-size: 25px;
    letter-spacing: 1px;
  }
  .gold-wave {
    position: absolute;
    top: 600px;
    left: 0;
    width: 100%;
    height: 160px;
    background: radial-gradient(ellipse 55% 35% at 55% 50%, rgba(240,199,119,0.75) 0%, rgba(201,154,76,0.45) 40%, rgba(138,90,30,0.15) 70%, rgba(0,0,0,0) 100%);
  }
  .claims {
    position: absolute;
    top: 810px;
    left: 80px;
    display: flex;
    gap: 40px;
  }
  .claim {
    width: 96px;
    display: flex;
    flex-direction: column;
    align-items: center;
    text-align: center;
    color: var(--text-grey);
    font-size: 16px;
    line-height: 1.25;
  }
  .claim svg { width: 54px; height: 54px; margin-bottom: 14px; }
  .net-weight-band {
    position: absolute;
    top: 1004px;
    left: 0;
    width: 100%;
    height: 64px;
    background: linear-gradient(90deg, var(--band-grey-light) 0%, var(--band-grey) 100%);
    display: flex;
    align-items: center;
    justify-content: center;
    color: var(--gold);
    font-size: 27px;
    letter-spacing: 2px;
  }
</style>
</head>
<body>
  <div class="label">
    <div class="gold-dust" role="img" aria-label="Fine gold sparkle dust"></div>

    <div class="brand-name">Corvella</div>

    <div class="range-band"><span class="range-name">REVITALIZING</span></div>

    <div class="product-name">SHAMPOO</div>
    <div class="key-ingredients">Ginseng &amp; Natural DHT</div>

    <div class="gold-wave" role="img" aria-label="Flowing golden light waves"></div>

    <div class="claims">
      <div class="claim">
        <svg viewBox="0 0 54 54" fill="none" stroke="var(--gold)" stroke-width="2">
          <circle cx="27" cy="27" r="25"/>
          <path d="M19 33 h16 v-6 a8 8 0 0 0 -16 0 z"/>
          <line x1="27" y1="19" x2="27" y2="15"/>
        </svg>
        <span>Fragrance<br>Free</span>
      </div>
      <div class="claim">
        <svg viewBox="0 0 54 54" fill="none" stroke="var(--gold)" stroke-width="2">
          <circle cx="27" cy="27" r="25"/>
          <ellipse cx="27" cy="27" rx="12" ry="5"/>
          <ellipse cx="27" cy="27" rx="12" ry="5" transform="rotate(60 27 27)"/>
          <ellipse cx="27" cy="27" rx="12" ry="5" transform="rotate(-60 27 27)"/>
          <circle cx="27" cy="27" r="1.5" fill="var(--gold)"/>
        </svg>
        <span>Sulfate<br>Free</span>
      </div>
      <div class="claim">
        <svg viewBox="0 0 54 54" fill="none" stroke="var(--gold)" stroke-width="2">
          <circle cx="27" cy="27" r="25"/>
          <line x1="20" y1="36" x2="32" y2="20"/>
          <path d="M31 17 l5 4 -3 3 -5 -4 z"/>
          <path d="M19 39 q-2 2 0 2 q2 0 0 -2"/>
        </svg>
        <span>No artificial<br>colors</span>
      </div>
    </div>

    <div class="net-weight-band">NET WT. &#8494; 473ML (16OZ.)</div>
  </div>
</body>
</html>
```